Need CATCHY/VIVID Banner design for my new UTV/ATV/Off Road Vehicle turn signal/lighting company

I need a banner ad designed so I can advertise on several different ATV (all terrain vehicle), UTV (Utility Vehicles), Golf Cart and Off-Road Vehicle forums. Ads need to be very catchy and produce a call to action. Action is getting hits to my website. Our main business is selling turn signal kits to make your side by side or your ATV/UTV street legal, as some states now allow you to drive these on public roads if you have the following items: Turn Signals, Horn, Lighted license plate bracket, headlights and brake lights. We sell all of these items for just about any model vehicle out there. Our call to action for this banner would be to get more website visits.

Target Market(s)

Off-road/outdoor enthusiasts,

Industry/Entity Type

Car Accessorie

Font styles to use
Sans Serif

Requirements
Must have
• Ad size need to be either 728x90 or 300x250. Colorful ad with an off-road vehicle integrated to the design (think UTV, side-by-side, etc.
Nice to have
• Nice to haves would be anything that makes this banner ad stand out on very boring web pages.
Should not have
• anything dull

```html
<!DOCTYPE html>
<html lang="en">
<head>
<meta charset="utf-8">
<title>ATV Vehicle Signal Lighting Banner</title>
<link rel="stylesheet" href="https://fonts.googleapis.com/css2?family=Roboto:wght@300;400;700;900&display=swap">
<style>
  :root {
    --red: #d41f1f;
    --red-deep: #c4161c;
    --orange-start: #e8401e;
    --orange-end: #f7941d;
    --white: #ffffff;
    --sand-light: #d9c3a3;
    --sand-mid: #a98c6b;
    --rock-dark: #5a4a3c;
    --sky: #c9d6df;
  }
  * { margin: 0; padding: 0; box-sizing: border-box; }
  html, body { width: 1200px; height: 148px; overflow: hidden; background: var(--white); }
  .banner {
    position: relative;
    width: 1200px;
    height: 148px;
    overflow: hidden;
    font-family: "Roboto", Arial, sans-serif;
    color: var(--white);
    background: var(--white);
  }
  .panel { position: absolute; top: 0; height: 148px; }
  .panel-photo {
    left: 0; width: 1200px;
    background:
      linear-gradient(180deg, var(--sky) 0%, var(--sand-light) 28%, var(--sand-mid) 60%, var(--rock-dark) 100%);
    clip-path: polygon(744px 0, 1200px 0, 1200px 148px, 688px 148px);
  }
  .panel-orange {
    left: 0; width: 1200px;
    background: linear-gradient(90deg, var(--orange-start) 30%, var(--orange-end) 62%);
    clip-path: polygon(328px 0, 736px 0, 680px 148px, 288px 148px);
  }
  .panel-red {
    left: 0; width: 330px;
    background: var(--red-deep);
    clip-path: polygon(0 0, 324px 0, 284px 148px, 0 148px);
  }
  .brand {
    position: absolute;
    left: 18px; width: 240px;
    top: 0;
    text-align: center;
  }
  .brand-name {
    display: inline-flex; align-items: center; gap: 8px;
    margin-top: 34px;
    font-size: 34px; font-weight: 900; letter-spacing: 0.5px;
    color: var(--white);
  }
  .brand-mark { width: 14px; height: 14px; background: var(--white); }
  .brand-tagline {
    position: absolute; left: 0; width: 240px;
    text-transform: uppercase; font-weight: 900; line-height: 1;
  }
  .tagline-main { top: 94px; font-size: 17.5px; letter-spacing: 0.2px; }
  .tagline-sub { top: 113px; font-size: 13px; letter-spacing: 0.3px; }
  .headline {
    position: absolute; left: 330px; width: 330px;
    text-align: center; text-transform: uppercase; line-height: 1;
  }
  .headline-top { top: 14px; font-size: 31px; font-weight: 300; letter-spacing: 0.5px; }
  .headline-main { top: 50px; font-size: 37px; font-weight: 700; letter-spacing: 0.3px; }
  .feature-icons {
    position: absolute; left: 336px; top: 100px;
    display: flex; gap: 32px; align-items: center;
  }
  .feature-icons svg { display: block; height: 30px; }
</style>
</head>
<body>
<div class="banner">
  <div class="panel panel-photo" role="img" aria-label="Photo of a red sport side-by-side UTV climbing desert rocks with a helmeted rider"></div>
  <div class="panel panel-orange"></div>
  <div class="panel panel-red"></div>

  <div class="brand">
    <div class="brand-name"><span class="brand-mark"></span>TrailBeam</div>
  </div>
  <div class="brand-tagline tagline-main" style="left:18px">Turn Signal Kits</div>
  <div class="brand-tagline tagline-sub" style="left:18px">&amp; Lighting Accessories</div>

  <div class="headline headline-top">ATV Vechicle</div>
  <div class="headline headline-main">Signal Lighting</div>

  <div class="feature-icons" aria-hidden="true">
    <svg viewBox="0 0 40 30" width="40">
      <g fill="none" stroke="#fff" stroke-width="2.6">
        <circle cx="20" cy="15" r="9"/>
        <path d="M8 4 A15 15 0 0 0 8 26"/>
        <path d="M32 4 A15 15 0 0 1 32 26"/>
      </g>
      <rect x="18.6" y="9" width="2.8" height="8" fill="#fff"/>
      <circle cx="20" cy="20.5" r="1.6" fill="#fff"/>
    </svg>
    <svg viewBox="0 0 40 30" width="40">
      <path d="M16 4 C6 4 4 10 4 15 C4 20 6 26 16 26 Z" fill="#fff"/>
      <g stroke="#fff" stroke-width="2.6" stroke-linecap="round">
        <line x1="22" y1="7" x2="36" y2="7"/>
        <line x1="22" y1="12" x2="36" y2="12"/>
        <line x1="22" y1="18" x2="36" y2="18"/>
        <line x1="22" y1="23" x2="36" y2="23"/>
      </g>
    </svg>
    <svg viewBox="0 0 50 30" width="50">
      <g stroke="#fff" stroke-width="2" stroke-linecap="round">
        <line x1="2" y1="15" x2="7" y2="15"/>
        <line x1="3" y1="7" x2="8" y2="10"/>
        <line x1="3" y1="23" x2="8" y2="20"/>
      </g>
      <path d="M11 4 L11 26 C18 22 26 18 36 18 L36 12 C26 12 18 8 11 4 Z" fill="none" stroke="#fff" stroke-width="2.4"/>
      <rect x="36" y="11" width="4" height="8" fill="#fff"/>
      <rect x="40" y="13" width="8" height="4" fill="#fff"/>
      <path d="M30 20 Q34 27 40 20" fill="#fff"/>
    </svg>
    <svg viewBox="0 0 60 30" width="60">
      <g fill="none" stroke="#fff" stroke-width="2.6" stroke-linejoin="round">
        <path d="M2 15 L14 4 L14 10 L26 10 L26 20 L14 20 L14 26 Z"/>
        <path d="M58 15 L46 4 L46 10 L34 10 L34 20 L46 20 L46 26 Z"/>
      </g>
    </svg>
    <svg viewBox="0 0 30 34" width="26">
      <rect x="8" y="2" width="14" height="30" rx="3" fill="#fff"/>
      <path d="M8 6 L2 6 L8 12 Z M8 15 L2 15 L8 21 Z M8 24 L2 24 L8 30 Z" fill="#fff"/>
      <path d="M22 6 L28 6 L22 12 Z M22 15 L28 15 L22 21 Z M22 24 L28 24 L22 30 Z" fill="#fff"/>
      <circle cx="15" cy="8" r="3" fill="#f08a1e"/>
      <circle cx="15" cy="17" r="3" fill="#f08a1e"/>
      <circle cx="15" cy="26" r="3" fill="#f08a1e"/>
    </svg>
  </div>
</div>
</body>
</html>
```